Modern and appealing business Wordpress site

I've been operating my consulting firm for 5 years and feel like it is time to really improve on my web presence as I'm starting to get more national attention. I had a logo made through this service a couple of years ago, and would like to get a website that matches the look of it. The website will be used to (1) advertise my services (2) provide a brief overview of our management philosophies, and (3) host a resource library database. I understand HTML, but am not as familiar with how to code Wordpress, so I need someone that can help upload themes.

The website can be found at www.trbvexlane.com.

For design, I prefer round designs to square and want the color scheme to match the attached logo. I have included both the full logo and the abbreviated one.

I also have a new picture for CFO uploaded. I plan on getting a new one for the CEO in the coming weeks, so I would like someone that I could get to help make the modification at a later time.

The resource database will be put into a document library (probably Plix4) once the final design is completed rather than having multiple pages with links...just so you know the final vision for the site.

Reach out if you have any questions.

Target Market(s)

Community Action Agencies, Nonprofit Organization Leaders

Industry/Entity Type

Consulting

Coding

Coded - Design and coding required

Font styles to use
Sans Serif

Requirements
Must have
• Must match the color scheme of the attached logo

```html
<!DOCTYPE html>
<html lang="en">
<head>
<meta charset="utf-8">
<title>TR Vexlane, LLC</title>
<link rel="stylesheet" href="https://fonts.googleapis.com/css2?family=Poppins:ital,wght@0,400;0,500;0,600;0,700;0,800;1,700&display=swap">
<style>
:root{
  --blue:#2f9fd8;
  --blue-soft:#cfe8f6;
  --ink:#4a4a4c;
  --text:#6b6b6e;
  --grey-bg:#f3f3f4;
  --footer:#545456;
  --footer-dark:#4a4a4c;
  --white:#ffffff;
}
*{margin:0;padding:0;box-sizing:border-box}
html,body{width:1200px;height:3946px;overflow:hidden}
body{font-family:'Poppins',sans-serif;color:var(--ink);background:var(--white);position:relative}
.abs{position:absolute}
.bg-shapes{position:absolute;left:0;top:0;width:1200px;height:3946px}
.brand{font-weight:700;font-size:30px;color:var(--blue);letter-spacing:1px;display:flex;align-items:center;gap:10px}
.nav{left:659px;top:32px;display:flex;gap:26px;font-size:13px;font-weight:500;color:var(--ink)}
.nav .active{color:var(--blue)}
.hero-title{left:88px;top:150px;font-size:67px;font-weight:800;line-height:66px;color:var(--ink)}
.hero-title span{color:var(--blue)}
.hero-text{left:88px;top:364px;width:390px;font-size:15px;line-height:23px;color:var(--text)}
.btn{left:88px;top:430px;width:140px;height:44px;border-radius:22px;background:var(--blue);color:#fff;font-size:12px;font-weight:600;display:flex;align-items:center;justify-content:center}
.band-word{left:0;width:1200px;top:780px;text-align:center;font-size:120px;font-weight:800;color:rgba(255,255,255,.18);letter-spacing:6px}
.band-mark{left:578px;top:870px;width:44px;height:44px;border-radius:50%;background:#fff}
.band-text{left:240px;width:720px;top:938px;text-align:center;color:#fff;font-size:23px;line-height:31px}
.h2{font-size:42px;font-weight:700;line-height:45px;color:var(--ink)}
.rule{width:50px;height:2px;background:#d8d8d8}
.para{font-size:14.5px;line-height:24px;color:var(--text)}
.card{width:254px;height:328px;top:1916px;background:#fff;border-radius:14px;box-shadow:0 6px 30px rgba(0,0,0,.06);text-align:center}
.card .icon{position:absolute;left:75px;top:38px;width:104px;height:104px;border-radius:50%}
.card .icon.blue{background:var(--blue)}
.card .icon.grey{background:var(--ink)}
.card .bub1{position:absolute;left:66px;top:48px;width:26px;height:26px;border-radius:50%;background:#e4e4e6}
.card .bub2{position:absolute;left:160px;top:112px;width:26px;height:26px;border-radius:50%;background:#e4e4e6}
.card h3{position:absolute;left:0;width:100%;top:164px;font-size:14px;font-weight:600;color:var(--ink)}
.card p{position:absolute;left:26px;width:202px;top:200px;font-size:13px;line-height:20.5px;color:var(--text)}
.person{background:#fff;box-shadow:0 6px 24px rgba(0,0,0,.08);text-align:center}
.person .photo{margin:6px auto 0;width:204px;height:190px}
.person h4{font-size:14px;font-weight:700;color:var(--ink);margin-top:14px}
.person small{display:block;font-size:11px;color:var(--text)}
.quote{left:567px;top:3024px;width:460px;font-size:23.5px;line-height:35.5px;font-weight:700;font-style:italic;color:var(--ink)}
.cite{left:567px;top:3207px;font-size:13px;font-weight:600;color:var(--blue)}
.arrow{top:3249px;width:50px;height:50px;border-radius:50%;background:#f1f1f2;display:flex;align-items:center;justify-content:center}
.f-title{font-size:16px;font-weight:700;color:#fff;top:3596px}
.f-list{list-style:none;top:3638px;left:415px;font-size:12.5px;color:#e6e6e6}
.f-list li{height:31px}
.f-list li::before{content:"›";margin-right:8px}
.contact{left:602px;font-size:12.5px;line-height:20px;color:#e6e6e6}
.contact svg{position:absolute;left:0;top:2px}
.contact div{padding-left:23px}
.social{top:3730px;width:42px;height:42px;border-radius:50%;background:#626264}
.input{left:849px;top:3691px;width:259px;height:46px;border-radius:23px;background:#fff;font-size:12px;color:#888;display:flex;align-items:center;padding-left:42px}
.copy{left:0;top:3886px;width:1200px;height:60px;background:var(--footer-dark);border-top:1px solid #606062;color:#fff;font-size:12px;font-weight:600;text-align:center;line-height:60px}
</style>
</head>
<body>

<svg class="bg-shapes" viewBox="0 0 1200 3946" aria-hidden="true">
  <path d="M0 690 C120 560 300 540 430 620 C600 740 850 800 1000 700 C1100 640 1170 600 1200 580 L1200 1111 L0 1111 Z" fill="var(--blue)"/>
  <path d="M0 600 C120 550 230 560 300 590 C200 580 90 610 0 690 Z" fill="var(--blue-soft)"/>
  <path d="M905 1111 C900 1050 980 990 1200 940 L1200 1155 C1060 1170 910 1160 905 1111 Z" fill="#d9ecf8"/>
  <path d="M0 2190 C80 2280 300 2300 600 2260 C900 2220 1050 2190 1200 2230 L1200 2880 C900 2900 700 2850 520 2780 C350 2720 150 2830 0 2760 Z" fill="var(--grey-bg)"/>
  <path d="M0 1750 C60 1780 120 1770 150 1740 L0 1815 Z" fill="var(--grey-bg)"/>
  <path d="M0 3420 C150 3380 260 3340 300 3300 C260 3370 150 3420 0 3440 Z" fill="var(--blue-soft)"/>
  <path d="M0 3420 C150 3560 380 3590 600 3520 C820 3450 1000 3400 1200 3440 L1200 3946 L0 3946 Z" fill="var(--footer)"/>
  <circle cx="920" cy="2614" r="235" fill="var(--blue)"/>
  <circle cx="735" cy="2332" r="11" fill="#a9d6ee"/>
  <circle cx="1089" cy="2408" r="6" fill="#a9d6ee"/>
  <circle cx="688" cy="2798" r="23" fill="#a9d6ee"/>
  <circle cx="1052" cy="2866" r="8" fill="#a9d6ee"/>
</svg>

<div class="abs brand" style="left:88px;top:20px">Vexlane</div>
<nav class="abs nav">
  <span class="active">HOME</span><span>SERVICES</span><span>LENS</span><span>PATH</span><span>RESOURCES</span><span>CONTACT</span>
</nav>

<h1 class="abs hero-title">START<br><span>SOMETHING</span><br>TOGETHER</h1>
<p class="abs hero-text">TR Vexlane, LLC was created to help nonprofits and government contractors meet their...</p>
<div class="abs btn">GET STARTED</div>
<div class="abs" role="img" aria-label="Team meeting around a conference table" style="left:533px;top:148px;width:700px;height:500px;border-radius:50%;transform:rotate(-14deg);background:linear-gradient(135deg,#d6d0c8,#8e7a68 60%,#5b4d44)"></div>

<div class="abs band-word">VEXLANE</div>
<div class="abs band-mark"></div>
<p class="abs band-text">TR Vexlane, LLC was created for one purpose – to ensure our customers are equipped with the tools necessary to achieve excellence. We are excited to hear about...</p>

<div class="abs" style="left:0;top:1200px;width:590px;height:540px;border-radius:40% 60% 58% 42% / 45% 50% 50% 55%;background:#d8ecf8"></div>
<div class="abs" role="img" aria-label="Three business colleagues standing together with a tablet" style="left:0;top:1195px;width:555px;height:540px;border-radius:30% 70% 62% 38% / 30% 52% 48% 70%;background:linear-gradient(135deg,#e8e8ea,#9a8e86 50%,#2e2e33)"></div>

<h2 class="abs h2" style="left:671px;top:1298px">LEADING<br>ORGANIZATIONS<br>TO EXCELLENCE!</h2>
<div class="abs rule" style="left:671px;top:1438px"></div>
<p class="abs para" style="left:671px;top:1457px;width:446px">TR Vexlane, LLC was created to help nonprofits and government contractors meet their basic funding requirements and adopt a Mission Aligned Data Driven mindset that promotes positive change in the lives of the people they serve. Our approach is not simply based off of theoretical business practices, but on practical solutions to real-life situations learned through more than twenty years of experience.</p>

<h2 class="abs h2" style="left:0;width:1200px;text-align:center;top:1776px">OUR SERVICES</h2>
<p class="abs para" style="left:300px;width:600px;text-align:center;top:1843px;font-size:14px;line-height:23px">Every service we provide is designed to ensure our customers are equipped with the tools they need to meet their basic funding requirements</p>

<div class="abs card" style="left:204px"><span class="bub1"></span><span class="bub2"></span><span class="icon blue"></span><h3>TRAINING &amp; CONSULTING</h3><p>We are dedicated to the success of our customers and offer a variety of services focused on improving...</p></div>
<div class="abs card" style="left:474px"><span class="bub1"></span><span class="bub2"></span><span class="icon grey"></span><h3>DATA ANALYTICS</h3><p>One the most important, and frequently neglected, areas of organizational management is the analysis of data...</p></div>
<div class="abs card" style="left:742px"><span class="bub1"></span><span class="bub2"></span><span class="icon blue"></span><h3>STORYTELLING</h3><p>TR Vexlane, LLC is dedicated to ensuring each of our customers is provided with the tools necessary to tell their...</p></div>

<div class="abs" style="left:45px;top:2470px;font-size:110px;font-weight:800;color:rgba(0,0,0,.05);line-height:110px">MISSION</div>
<h2 class="abs h2" style="left:124px;top:2572px">OUR MISSION</h2>
<div class="abs rule" style="left:124px;top:2626px"></div>
<p class="abs para" style="left:124px;top:2645px;width:440px;font-size:14px">To help social service organizations develop a Mission Aligned Data Driven mindset that promotes positive change in the lives of the customers they serve.</p>

<div class="abs person" style="left:612px;top:2372px;width:216px;height:257px">
  <div class="photo" role="img" aria-label="Portrait of the CEO" style="background:linear-gradient(180deg,#4a5870,#26324a)"></div>
  <h4>OUR CEO</h4><small>Dorian “Reed” Vexlane</small>
</div>
<div class="abs person" style="left:854px;top:2470px;width:216px;height:282px">
  <div class="photo" role="img" aria-label="Portrait of the CFO" style="margin-top:6px;height:208px;background:linear-gradient(180deg,#6b7f8c,#3e5866)"></div>
  <h4 style="margin-top:16px">OUR CFO</h4><small>Marisol Keane Vexlane</small>
</div>

<div class="abs" role="img" aria-label="Two colleagues reviewing a document together" style="left:184px;top:2974px;width:346px;height:346px;border-radius:50%;background:linear-gradient(135deg,#e4ddd4,#a48a74 55%,#6a5648)"></div>
<div class="abs" style="left:670px;top:2870px;font-size:260px;font-weight:800;line-height:260px;color:rgba(0,0,0,.05)">“</div>
<p class="abs quote">“Reed is easy to work with and his expertise allows you to tailor your training to the specific needs of your agency. We highly recommend Reed and his company.”</p>
<div class="abs cite">-Community Action Network of Upper Valley</div>
<div class="abs arrow" style="left:567px"><svg width="12" height="12" viewBox="0 0 12 12"><path d="M8 2 4 6l4 4" fill="none" stroke="#333" stroke-width="1.6"/></svg></div>
<div class="abs arrow" style="left:622px"><svg width="12" height="12" viewBox="0 0 12 12"><path d="M4 2l4 4-4 4" fill="none" stroke="#333" stroke-width="1.6"/></svg></div>

<div class="abs brand" style="left:88px;top:3658px;color:#fff;font-size:40px">Vexlane</div>
<span class="abs social" style="left:115px"></span>
<span class="abs social" style="left:166px"></span>
<span class="abs social" style="left:217px"></span>
<span class="abs social" style="left:267px"></span>

<div class="abs f-title" style="left:415px">QUICK LINKS</div>
<ul class="abs f-list"><li>HOME</li><li>SERVICES</li><li>LENS</li><li>PATH</li><li>RESOURCES</li><li>CONTACT</li></ul>

<div class="abs f-title" style="left:602px">CONTACT INFO</div>
<div class="abs contact" style="top:3636px"><svg width="14" height="12" viewBox="0 0 14 12"><rect x="1" y="1" width="12" height="10" fill="none" stroke="var(--blue)" stroke-width="1.5"/><path d="M1 1l6 5 6-5" fill="none" stroke="var(--blue)" stroke-width="1.5"/></svg><div>Email:<br>info@trbvexlane.com</div></div>
<div class="abs contact" style="top:3698px"><svg width="14" height="14" viewBox="0 0 14 14"><path d="M3 1l3 3-2 2c1 2 2 3 4 4l2-2 3 3-2 2C6 13 1 8 1 3Z" fill="var(--blue)"/></svg><div>Phone:<br>(555) 014-2287</div></div>
<div class="abs contact" style="top:3760px"><svg width="12" height="15" viewBox="0 0 12 15"><path d="M6 1a5 5 0 0 1 5 5c0 4-5 8-5 8S1 10 1 6a5 5 0 0 1 5-5Z" fill="var(--blue)"/><circle cx="6" cy="6" r="2" fill="#545456"/></svg><div>Location:<br>418 Marrow Lane<br>Elmsford, Ohio 45012</div></div>

<div class="abs f-title" style="left:851px">NEWSLETTER</div>
<p class="abs" style="left:851px;top:3636px;width:260px;font-size:12.5px;line-height:18px;color:#e6e6e6">Subscribe to our email address to get the latest news.</p>
<div class="abs input">Enter Your Email...</div>
<div class="abs" style="left:1062px;top:3691px;width:46px;height:46px;border-radius:0 23px 23px 0;background:var(--blue);display:flex;align-items:center;justify-content:center"><svg width="16" height="16" viewBox="0 0 16 16"><path d="M1 7 15 1 10 15 7 9Z" fill="#fff"/></svg></div>

<div class="abs copy">© COPYRIGHT 2022 | ALL RIGHTS RESERVED</div>
<div class="abs" style="left:1106px;top:3855px;width:54px;height:54px;border-radius:50%;background:var(--blue);display:flex;align-items:center;justify-content:center"><svg width="24" height="22" viewBox="0 0 24 22"><path d="M12 2C6 2 2 5.5 2 10c0 2.4 1.2 4.4 3 5.8V20l4-2.3c1 .2 2 .3 3 .3 6 0 10-3.5 10-8S18 2 12 2Z" fill="#fff"/></svg></div>

</body>
</html>
```